I am looking for a web design that includes space for a blog, archive and an
“ about me” section. It should be capable of being updated in the future should I decide to build the site. I like edgy, creative, friendly and inviting to go with my logo style.
The Pantry Compass is an approach to breaking down and rebuilding or just tweaking what needs to be done to reach nutritional fitness. That is the actual workout part....journaling through something I call reflective nutrition. By doing this one can actually see what they are doing well and where they may need to improve. It involves goal setting and analyzing one's relationship with food. the workout is more mental in this approach. Physical activity is definitely a part of a strong nutritional foundation, but here I am focusing on the work that goes into creating a positive nutritionally fit person.

1. Blog Section: this will be the foundation of the website. I will write weekly blogs explaining and encouraging readers to use reflective nutrition approach to discover and explore their relationship with food and create healthy nutritional habits, breaking those that have been detrimental thus far. Journaling and realistic goal setting is the key to this approach.

2. Archive: this is the section to store old blogs by date with ability to retrieve and read again. Readers should gave access to this section.

3. About Me: I am a clinical nutritionist with a Bachelors of Science and Masters of Science in Nutrition. I have over 30 years experience working with both inpatient and outpatient populations covering a myriad of conditions requiring nutritional intervention. I am passionate about my field and my goal is to help others achieve their optimal nutritional health. I will share my personal struggle with attaining nutritional fitness. I have the
unique perspective of being both a nutrition professional and patient.
Please note that my blog name is not the name under which I am registered with the Bureau For Dietary Licensing (BDL).Contact me privately if you require more information.
Thank you for stopping by and I hope you will come back.
Peace,
M. Harlow
4. Contact Me: This section will only contain my email address for comments and suggestions Thepantrycompass@mailvento.net
Updates

Hey guys! I am very new to this process and I apologize for not having much detail. I think I added more that may give you a clearer understanding of my project. I know I said that I didn't plan on using illustrations but I am getting a better picture of what you do. Please use all your creative tools and talents and imaginations! But read my description of what the actual pantry compass is. It is more of a mental not physical workout. I will respond to your questions and suggestions. I welcome them. Have fun with this!!! I look forward to seeing your work. . Peace, Mara

Target Market(s)

Anyone interested in a realistic approach to reaching nutrition goals.

Industry/Entity Type

Nutrition

Coding

Coded - Design and coding required

Number of Pages Required

3 page

Colors
fbee3d
ffc214

Requirements
Must have
• An automatic sign-off signature at the end of each blog, preferably in the same font as my logo name. Signature will read:
Peace,
M.
My blog name is M, Harlow
Complementary color scheme to the logo but not white, if at all possible. I don't plan on using illustrations so I am relying on the web design to draw people in. It cannot be dull or bland but still professional.
It must be inviting and personable, not intimidating
I may want to update and add on later. Site should be capable of doing
that....should be buildable.
I love the font that was used in the name of my logo and would like to stay consistant with that, if possible.
Nice to have
• A way to monitor people who visit and return.
Maybe a counter to see how many people have visited
Would it be possible to prominently display my logo on the first page with my contact information and have that open directly to my blog page? Also, would the block page have to be a white background? I prefer it to be a color if that is complementary to the logo olor scheme
Should not have
• Please no illustrations of a gym.
This isn’t a blog about physical fitness. It is a blog requiring people to think about what they consume on a daily basis, breaking bad eating habits and creating positive, healthy ones.
I tried to get pictures and illustrations to use but due to licensure restrictions, I was unable at this time. Although your designs are brilliant, I may not be able to supply appropriate illustrations to do your designs justice.

```html
<!DOCTYPE html>
<html lang="en">
<head>
<meta charset="utf-8">
<title>The Pantry Compass – Site Pages</title>
<link rel="stylesheet" href="https://fonts.googleapis.com/css2?family=Poppins:wght@400;500;600;700&family=Tinos&family=Roboto:wght@400;500&display=swap">
<style>
:root{
  --gold:#c9ab1c;
  --gold-dark:#b89b12;
  --ink:#1c1c1c;
  --muted:#555;
  --cream:#f8f4e3;
  --stage:#6e6e6e;
  --white:#fff;
  --blue:#4a84f2;
  --line:#d4d4d4;
}
*{box-sizing:border-box;margin:0;padding:0}
html,body{width:1200px;height:1016px;overflow:hidden}
body{background:var(--stage);position:relative;font-family:'Poppins',sans-serif;color:var(--ink)}
.page{position:absolute;top:39px;width:645px;background:var(--white);transform:scale(.5758);transform-origin:0 0;box-shadow:0 6px 20px rgba(0,0,0,.35);overflow:hidden}
.page--home{left:22px;height:1628px}
.page--captcha{left:413px;height:1628px}
.page--contact{left:807px;height:812px}
.abs{position:absolute}

/* header */
.site-header{position:absolute;left:0;top:0;width:645px;height:44px;background:var(--white);z-index:2}
.brand-tab{position:absolute;left:45px;top:0;width:66px;height:85px;background:var(--white);clip-path:polygon(0 0,100% 0,100% 86%,0 100%);z-index:3;display:flex;flex-direction:column;align-items:center;padding-top:10px;gap:5px}
.brand-tab__dot{width:22px;height:22px;border-radius:50%;background:var(--gold)}
.brand-tab__name{font-size:8px;font-weight:600;color:var(--gold);text-align:center;line-height:1.1}
.main-nav{position:absolute;top:25px;display:flex;gap:21px;font-size:7.5px;color:#333}

/* hero */
.hero{position:absolute;left:0;top:44px;width:645px;height:202px;background:radial-gradient(circle at 78% 40%,#a77c47 0,#6e5233 22%,rgba(58,58,62,0) 45%),linear-gradient(120deg,#2e2f33,#3c3e43)}
.hero__mark{position:absolute;left:108px;top:100px;width:110px;height:110px;border-radius:50%;background:var(--gold)}
.hero__title{position:absolute;left:234px;top:118px;font-size:31px;font-weight:600;color:var(--white)}
.tab-btn{position:absolute;background:var(--gold);color:var(--white);font-size:7.5px;font-weight:700;display:flex;align-items:center;justify-content:center;border-radius:9px 9px 0 0;letter-spacing:.2px}

/* intro */
.intro-col{position:absolute;top:274px;width:150px}
.intro-col h3{font-size:11px;font-weight:600;margin-bottom:8px}
.intro-col p{font-family:'Tinos',serif;font-size:6.3px;line-height:12px;color:#333}

/* about */
.about__script{position:absolute;left:240px;top:455px;width:160px;height:56px;background:linear-gradient(90deg,rgba(0,0,0,0),rgba(0,0,0,.05),rgba(0,0,0,0))}
.about__title{position:absolute;left:0;width:645px;top:486px;text-align:center;font-size:20px;font-weight:600;color:var(--gold)}
.about__text{position:absolute;left:100px;top:522px;width:445px;text-align:center;font-family:'Tinos',serif;font-size:6.3px;line-height:12px;color:#222}
.about__text a{color:#3b6fd8;text-decoration:none}

/* blog */
.band{position:absolute;left:0;width:645px;background:var(--gold)}
.section-title{position:absolute;left:0;width:645px;text-align:center;font-weight:700}
.blog-card{position:absolute;top:677px;width:177px;height:181px;background:var(--white);padding:17px 11px 0;box-shadow:0 2px 5px rgba(0,0,0,.15)}
.blog-card__tags{font-size:5px;color:#444;display:flex;gap:10px}
.blog-card__cat{font-size:5px;color:var(--gold);font-weight:600;margin-top:5px}
.blog-card h4{font-size:10.5px;font-weight:600;line-height:13.5px;margin:6px 0 7px}
.blog-card p{font-family:'Tinos',serif;font-size:6.1px;line-height:12px;color:#333;padding-left:2px}
.blog-card__foot{position:absolute;left:8px;right:8px;bottom:12px;border-top:1px solid #e6e1c8;padding-top:8px;font-size:5.5px;color:#999;display:flex;justify-content:space-between;align-items:center}
.ico-box{display:inline-block;width:9px;height:7px;border:1px solid #bbb;margin-right:4px;vertical-align:middle}

/* archive */
.archive-card{position:absolute;background:var(--gold);padding:14px 13px;box-shadow:0 2px 5px rgba(0,0,0,.2)}
.archive-card h4{font-size:10.5px;font-weight:600;line-height:13.5px;color:#2a2410;margin-bottom:9px}
.archive-card p{font-family:'Tinos',serif;font-size:6.1px;line-height:12px;color:#fffbe3;margin-bottom:9px}
.archive-card__date{font-size:5.5px;color:#fffbe3}
.archive-card__date .ico-box{border-color:#fffbe3}

/* partners */
.partner{position:absolute;font-size:10px;font-weight:700;color:var(--white)}

/* footer */
.foot-title{position:absolute;font-size:13px;font-weight:600}
.foot-list{position:absolute;list-style:none;font-size:7px;color:#333}
.foot-list li{display:flex;gap:12px;margin-bottom:12px;line-height:11px}
.foot-list svg{flex:none}
.foot-menu li{margin-bottom:7px}
.foot-menu li::before{content:"›";color:var(--gold);margin-right:12px}
.foot-brand{position:absolute;display:flex;flex-direction:column;align-items:center;gap:6px;width:90px}
.foot-brand__dot{width:40px;height:40px;border-radius:50%;background:var(--gold)}
.foot-brand__name{font-size:12px;font-weight:600;color:var(--gold);text-align:center;line-height:1.15}
.social{display:flex;gap:10px;margin-top:4px}
.social span{width:9px;height:9px;border-radius:50%;background:var(--gold)}
.copyright{position:absolute;left:0;width:645px;text-align:center;font-size:5.5px;color:#333}

/* captcha modal */
.shade{position:absolute;inset:0;background:rgba(25,25,25,.62);z-index:5}
.modal{position:absolute;left:40px;top:504px;width:566px;height:346px;background:var(--white);z-index:6;font-family:'Roboto',sans-serif}
.check-card{position:absolute;left:23px;top:16px;width:265px;height:58px;border:1px solid var(--line);border-radius:3px;box-shadow:0 1px 3px rgba(0,0,0,.12);background:#f9f9f9}
.check-card__box{position:absolute;left:14px;top:17px;width:24px;height:24px;border:2px solid #c1c1c1;border-radius:2px;background:var(--white)}
.check-card__label{position:absolute;left:49px;top:22px;font-size:10px;color:#222}
.check-card__badge{position:absolute;right:14px;top:8px;width:40px;text-align:center;font-size:4.5px;color:#666;line-height:6px}
.check-card__badge span{display:block;width:14px;height:14px;margin:0 auto 4px;background:#9fb3d8}
.grey-btn{position:absolute;left:28px;top:95px;width:64px;height:24px;background:#9e9e9e;color:var(--white);font-size:8px;display:flex;align-items:center;justify-content:center;border-radius:2px}
.challenge{position:absolute;left:300px;top:16px;width:243px;height:315px;border:1px solid #ccc;box-shadow:0 1px 4px rgba(0,0,0,.15)}
.challenge__head{position:absolute;left:7px;top:5px;width:229px;height:67px;background:var(--blue);color:var(--white);padding:14px 14px}
.challenge__head small{display:block;font-size:7px}
.challenge__head strong{display:block;font-size:18px;font-weight:400;margin-top:3px}
.tile-grid{position:absolute;left:7px;top:76px;display:grid;grid-template-columns:repeat(3,73px);grid-auto-rows:62px;gap:5px 5px}
.tile{display:block}
.challenge__foot{position:absolute;left:0;right:0;top:282px;border-top:1px solid #ddd;height:33px}
.challenge__icons{position:absolute;left:12px;top:11px;display:flex;gap:6px}
.challenge__icons span{width:7px;height:7px;border-radius:50%;border:1.5px solid #666}
.verify-btn{position:absolute;right:7px;top:4px;width:64px;height:24px;background:var(--blue);color:var(--white);font-size:8px;font-weight:500;display:flex;align-items:center;justify-content:center;border-radius:2px}

/* contact page */
.cream{position:absolute;left:0;top:60px;width:645px;height:440px;background:var(--cream)}
.crumbs{position:absolute;left:49px;top:103px;font-family:'Tinos',serif;font-size:6px;display:flex;gap:7px}
.crumbs .current{color:#3b6fd8}
.form-title{position:absolute;left:0;width:645px;top:140px;text-align:center;font-size:20px;font-weight:600}
.form-title__rule{position:absolute;left:313px;top:172px;width:26px;height:2px;background:var(--gold)}
.field{position:absolute;border:1px solid #c9c3a8;background:var(--cream);font-size:5.8px;color:#333;padding:10px 12px;box-shadow:inset 0 0 0 1px #fff}
.submit-btn{position:absolute;left:268px;top:408px;width:110px;height:28px;border-radius:14px;background:var(--gold);color:#1c1c1c;font-size:8px;font-weight:700;display:flex;align-items:center;justify-content:center;box-shadow:0 4px 6px rgba(0,0,0,.3)}
</style>
</head>
<body>

<section class="page page--home" aria-label="Home page">
  <header class="site-header">
    <nav class="main-nav" style="left:315px"><span>Home</span><span>About Me</span><span>Services</span><span>Blog</span><span>Contact Us</span></nav>
  </header>
  <div class="brand-tab"><span class="brand-tab__dot"></span><span class="brand-tab__name">The Pantry<br>Compass</span></div>
  <div class="hero" role="img" aria-label="Desk scene with a spiral notebook, pencil and snacks on a dark table"></div>
  <span class="hero__mark abs"></span>
  <div class="hero__title">The Pantry Compass</div>
  <div class="tab-btn" style="left:247px;top:173px;width:90px;height:24px">READ MORE</div>

  <div class="intro-col" style="left:71px"><h3>Lorem ipsum</h3><p>Quis autem vel eum iure reprehenderit qui in ea voluptate velit esse quam nihil molestiae consequatur, vel illum qui dolorem eum fugiat quo voluptas nulla pariatur</p></div>
  <div class="intro-col" style="left:249px"><h3>Lorem ipsum</h3><p>Quis autem vel eum iure reprehenderit qui in ea voluptate velit esse quam nihil molestiae consequatur, vel illum qui dolorem eum fugiat quo voluptas nulla pariatur</p></div>
  <div class="intro-col" style="left:434px"><h3>Lorem ipsum</h3><p>Quis autem vel eum iure reprehenderit qui in ea voluptate velit esse quam nihil molestiae consequatur, vel illum qui dolorem eum fugiat quo voluptas nulla pariatur</p></div>
  <div class="tab-btn" style="left:257px;top:381px;width:131px;height:24px">NUTRITIONAL FACTS</div>

  <div class="about__script" role="img" aria-label="Faint handwritten signature"></div>
  <h2 class="about__title">About Me</h2>
  <p class="about__text">I am a clinical nutritionist with a Bachelors of Science and Masters of Science in Nutrition. I have over 30 years experience working with both inpatient and outpatient populations covering a myriad of conditions requiring nutritional intervention. I am passionate about my field and my goal is to help others achieve their optimal nutritional health.My blog name, Harlow, is not the name I am registered under with The Bureau For Dietary Licensing (BDL).If you require more information, please <a href="#">click here.</a></p>

  <div class="band" style="top:595px;height:306px"></div>
  <h2 class="section-title" style="top:620px;font-size:26px;color:#fff">Blog</h2>
  <article class="blog-card" style="left:40px"><div class="blog-card__tags"><span>INFORMATIONAL</span><span>FITNESS TIPS</span></div><div class="blog-card__cat">NUTRITION</div><h4>Nor again is there anyone who loves or pursues or desires to obtain</h4><p>Quis autem vel eum iure reprehenderit qui in ea voluptate velit esse quam nihil molestiae consequatur, vel illum qui dolorem eum fugiat quo voluptas nulla pariatur</p><div class="blog-card__foot"><span><i class="ico-box"></i>Feb 10, 2021</span><i class="ico-box"></i></div></article>
  <article class="blog-card" style="left:234px"><div class="blog-card__tags"><span>INFORMATIONAL</span><span>FITNESS TIPS</span></div><div class="blog-card__cat">NUTRITION</div><h4>Nor again is there anyone who loves or pursues or desires to obtain</h4><p>Quis autem vel eum iure reprehenderit qui in ea voluptate velit esse quam nihil molestiae consequatur, vel illum qui dolorem eum fugiat quo voluptas nulla pariatur</p><div class="blog-card__foot"><span><i class="ico-box"></i>Feb 10, 2021</span><i class="ico-box"></i></div></article>
  <article class="blog-card" style="left:428px"><div class="blog-card__tags"><span>INFORMATIONAL</span><span>FITNESS TIPS</span></div><div class="blog-card__cat">NUTRITION</div><h4>Nor again is there anyone who loves or pursues or desires to obtain</h4><p>Quis autem vel eum iure reprehenderit qui in ea voluptate velit esse quam nihil molestiae consequatur, vel illum qui dolorem eum fugiat quo voluptas nulla pariatur</p><div class="blog-card__foot"><span><i class="ico-box"></i>Feb 10, 2021</span><i class="ico-box"></i></div></article>

  <div class="tab-btn" style="left:257px;top:927px;width:131px;height:25px">VIEW MORE BLOG</div>
  <h2 class="section-title" style="top:975px;font-size:27px">Archive</h2>
  <article class="archive-card" style="left:39px;top:1036px;width:276px;height:246px"><h4>Nor again is there anyone who loves or pursues or desires to obtain</h4><p>But I must explain to you how all this mistaken idea of denouncing pleasure and praising pain was born and</p><p>I will give you a complete account of the system, and expound the actual teachings of the great explorer of the truth, the master-builder of human happiness.Nor again is there anyone who loves or pursues or desires to obtain pain of...</p><p>Lorem ipsum dolor sit amet, consectetur adipiscing elit, sed do eiusmod tempor incididunt ut labore et dolore magna aliqua. Ut enim ad minim veniam, quis nostrud exercitation ullamco laboris nisi ut aliquip ex ea commodo consequat.</p><div class="archive-card__date"><i class="ico-box"></i>Jan 10, 2020</div></article>
  <article class="archive-card" style="left:329px;top:1036px;width:275px;height:116px"><h4>Nor again is there anyone who loves or pursues or desires to obtain</h4><p>Quis autem vel eum iure reprehenderit qui in ea voluptate velit esse quam nihil molestiae consequatur, vel illum qui dolorem eum fugiat quo voluptas nulla pariatur</p><div class="archive-card__date"><i class="ico-box"></i>Jan 10, 2020</div></article>
  <article class="archive-card" style="left:329px;top:1166px;width:275px;height:116px"><h4>Nor again is there anyone who loves or pursues or desires to obtain</h4><p>Quis autem vel eum iure reprehenderit qui in ea voluptate velit esse quam nihil molestiae consequatur, vel illum qui dolorem eum fugiat quo voluptas nulla pariatur</p><div class="archive-card__date"><i class="ico-box"></i>Jan 10, 2020</div></article>

  <div class="band" style="top:1318px;height:81px"></div>
  <span class="partner" style="left:73px;top:1352px">Oakmere</span>
  <span class="partner" style="left:187px;top:1354px">Brightvale</span>
  <span class="partner" style="left:305px;top:1354px">Tallwick</span>
  <span class="partner" style="left:430px;top:1354px">Ferncourt</span>
  <span class="partner" style="left:522px;top:1354px">Quillory</span>

  <h3 class="foot-title" style="left:49px;top:1432px">Contact Us</h3>
  <ul class="foot-list" style="left:49px;top:1470px">
    <li><svg width="9" height="11" viewBox="0 0 9 11"><path d="M4.5 0A4 4 0 0 0 .5 4c0 3 4 7 4 7s4-4 4-7a4 4 0 0 0-4-4zm0 5.5a1.5 1.5 0 1 1 0-3 1.5 1.5 0 0 1 0 3z" fill="#c9ab1c"/></svg><span>Dolore magnam aliquam<br>quaerat voluptatem.</span></li>
    <li><svg width="10" height="10" viewBox="0 0 10 10"><path d="M2 0l2 2.5-1 1.3a6 6 0 0 0 3.2 3.2L7.5 6 10 8 8.6 10C4 10 0 6 0 1.4z" fill="#c9ab1c"/></svg><span>0800 410 22 73<br>0900 731 45 08</span></li>
    <li><svg width="10" height="8" viewBox="0 0 10 8"><rect width="10" height="8" fill="#c9ab1c"/><path d="M0 0l5 4 5-4" stroke="#fff" fill="none"/></svg><span>Thepantrycompass@mailvento.net</span></li>
  </ul>
  <h3 class="foot-title" style="left:273px;top:1432px">Menu</h3>
  <ul class="foot-list foot-menu" style="left:275px;top:1470px"><li>Home</li><li>About Me</li><li>Services</li><li>Blog</li><li>Contact Us</li></ul>
  <div class="foot-brand" style="left:448px;top:1432px"><span class="foot-brand__dot"></span><span class="foot-brand__name">The Pantry<br>Compass</span><div class="social" aria-label="Social links"><span></span><span></span><span></span></div></div>
  <p class="copyright" style="top:1608px">© 2021 &nbsp;|&nbsp; www.pantrycompass.net</p>
</section>

<section class="page page--captcha" aria-label="Home page with verification dialog">
  <header class="site-header">
    <nav class="main-nav" style="left:315px"><span>Home</span><span>About Me</span><span>Services</span><span>Blog</span><span>Contact Us</span></nav>
  </header>
  <div class="brand-tab"><span class="brand-tab__dot"></span><span class="brand-tab__name">The Pantry<br>Compass</span></div>
  <div class="hero" role="img" aria-label="Desk scene with a spiral notebook, pencil and snacks on a dark table"></div>
  <span class="hero__mark abs"></span>
  <div class="hero__title">The Pantry Compass</div>
  <div class="tab-btn" style="left:247px;top:173px;width:90px;height:24px">READ MORE</div>

  <div class="intro-col" style="left:71px"><h3>Lorem ipsum</h3><p>Quis autem vel eum iure reprehenderit qui in ea voluptate velit esse quam nihil molestiae consequatur, vel illum qui dolorem eum fugiat quo voluptas nulla pariatur</p></div>
  <div class="intro-col" style="left:249px"><h3>Lorem ipsum</h3><p>Quis autem vel eum iure reprehenderit qui in ea voluptate velit esse quam nihil molestiae consequatur, vel illum qui dolorem eum fugiat quo voluptas nulla pariatur</p></div>
  <div class="intro-col" style="left:434px"><h3>Lorem ipsum</h3><p>Quis autem vel eum iure reprehenderit qui in ea voluptate velit esse quam nihil molestiae consequatur, vel illum qui dolorem eum fugiat quo voluptas nulla pariatur</p></div>
  <div class="tab-btn" style="left:257px;top:381px;width:131px;height:24px">NUTRITIONAL FACTS</div>
  <div class="about__script" role="img" aria-label="Faint handwritten signature"></div>
  <h2 class="about__title">About Me</h2>

  <div class="band" style="top:595px;height:306px"></div>
  <div class="tab-btn" style="left:257px;top:927px;width:131px;height:25px">VIEW MORE BLOG</div>
  <h2 class="section-title" style="top:975px;font-size:27px">Archive</h2>
  <article class="archive-card" style="left:39px;top:1036px;width:276px;height:246px"><h4>Nor again is there anyone who loves or pursues or desires to obtain</h4><p>But I must explain to you how all this mistaken idea of denouncing pleasure and praising pain was born and</p><p>I will give you a complete account of the system, and expound the actual teachings of the great explorer of the truth, the master-builder of human happiness.Nor again is there anyone who loves or pursues or desires to obtain pain of...</p><p>Lorem ipsum dolor sit amet, consectetur adipiscing elit, sed do eiusmod tempor incididunt ut labore et dolore magna aliqua. Ut enim ad minim veniam, quis nostrud exercitation ullamco laboris nisi ut aliquip ex ea commodo consequat.</p><div class="archive-card__date"><i class="ico-box"></i>Jan 10, 2020</div></article>
  <article class="archive-card" style="left:329px;top:1036px;width:275px;height:116px"><h4>Nor again is there anyone who loves or pursues or desires to obtain</h4><p>Quis autem vel eum iure reprehenderit qui in ea voluptate velit esse quam nihil molestiae consequatur, vel illum qui dolorem eum fugiat quo voluptas nulla pariatur</p><div class="archive-card__date"><i class="ico-box"></i>Jan 10, 2020</div></article>
  <article class="archive-card" style="left:329px;top:1166px;width:275px;height:116px"><h4>Nor again is there anyone who loves or pursues or desires to obtain</h4><p>Quis autem vel eum iure reprehenderit qui in ea voluptate velit esse quam nihil molestiae consequatur, vel illum qui dolorem eum fugiat quo voluptas nulla pariatur</p><div class="archive-card__date"><i class="ico-box"></i>Jan 10, 2020</div></article>

  <div class="band" style="top:1318px;height:81px"></div>
  <span class="partner" style="left:73px;top:1352px">Oakmere</span>
  <span class="partner" style="left:187px;top:1354px">Brightvale</span>
  <span class="partner" style="left:305px;top:1354px">Tallwick</span>
  <span class="partner" style="left:430px;top:1354px">Ferncourt</span>
  <span class="partner" style="left:522px;top:1354px">Quillory</span>

  <h3 class="foot-title" style="left:49px;top:1432px">Contact Us</h3>
  <ul class="foot-list" style="left:49px;top:1470px">
    <li><svg width="9" height="11" viewBox="0 0 9 11"><path d="M4.5 0A4 4 0 0 0 .5 4c0 3 4 7 4 7s4-4 4-7a4 4 0 0 0-4-4zm0 5.5a1.5 1.5 0 1 1 0-3 1.5 1.5 0 0 1 0 3z" fill="#c9ab1c"/></svg><span>Dolore magnam aliquam<br>quaerat voluptatem.</span></li>
    <li><svg width="10" height="10" viewBox="0 0 10 10"><path d="M2 0l2 2.5-1 1.3a6 6 0 0 0 3.2 3.2L7.5 6 10 8 8.6 10C4 10 0 6 0 1.4z" fill="#c9ab1c"/></svg><span>0800 410 22 73<br>0900 731 45 08</span></li>
    <li><svg width="10" height="8" viewBox="0 0 10 8"><rect width="10" height="8" fill="#c9ab1c"/><path d="M0 0l5 4 5-4" stroke="#fff" fill="none"/></svg><span>Thepantrycompass@mailvento.net</span></li>
  </ul>
  <h3 class="foot-title" style="left:273px;top:1432px">Menu</h3>
  <ul class="foot-list foot-menu" style="left:275px;top:1470px"><li>Home</li><li>About Me</li><li>Services</li><li>Blog</li><li>Contact Us</li></ul>
  <div class="foot-brand" style="left:448px;top:1432px"><span class="foot-brand__dot"></span><span class="foot-brand__name">The Pantry<br>Compass</span><div class="social" aria-label="Social links"><span></span><span></span><span></span></div></div>
  <p class="copyright" style="top:1608px">© 2021 &nbsp;|&nbsp; www.pantrycompass.net</p>

  <div class="shade"></div>
  <div class="modal" role="dialog" aria-label="Visitor verification">
    <div class="check-card">
      <span class="check-card__box"></span>
      <span class="check-card__label">I'm not a robot</span>
      <div class="check-card__badge"><span></span>CheckGate<br>Privacy - Terms</div>
    </div>
    <div class="grey-btn">SUBMIT</div>
    <div class="challenge">
      <div class="challenge__head"><small>Select the Images with</small><strong>Cycles</strong></div>
      <div class="tile-grid">
        <span class="tile" role="img" aria-label="Street with parked bicycles" style="background:linear-gradient(#b98a5c,#6d5a45)"></span>
        <span class="tile" role="img" aria-label="Fallen bicycle on pavement" style="background:linear-gradient(#8c7e70,#3f3a36)"></span>
        <span class="tile" role="img" aria-label="Rider beside a motorbike" style="background:linear-gradient(#5a5e66,#2b2c30)"></span>
        <span class="tile" role="img" aria-label="Narrow city street" style="background:linear-gradient(#a89a8a,#4b4640)"></span>
        <span class="tile" role="img" aria-label="Motorbike in a dark alley" style="background:linear-gradient(#5b4034,#231c1a)"></span>
        <span class="tile" role="img" aria-label="Bicycles outside a shopfront" style="background:linear-gradient(#6f6256,#3a332e)"></span>
        <span class="tile" role="img" aria-label="Bicycle against a pale wall" style="background:linear-gradient(#c8ccc6,#7b8a86)"></span>
        <span class="tile" role="img" aria-label="Blue car at sunset" style="background:linear-gradient(#d9a35a,#2f5f9a)"></span>
        <span class="tile" role="img" aria-label="Busy street at night" style="background:linear-gradient(#8a5a3c,#2a1e1a)"></span>
      </div>
      <div class="challenge__foot">
        <div class="challenge__icons"><span></span><span></span><span></span></div>
        <div class="verify-btn">VERIFY</div>
      </div>
    </div>
  </div>
</section>

<section class="page page--contact" aria-label="Contact page">
  <header class="site-header" style="height:60px">
    <nav class="main-nav" style="left:315px;top:28px"><span>Home</span><span>About Me</span><span>Services</span><span>Blog</span><span>Contact Us</span></nav>
  </header>
  <div class="brand-tab"><span class="brand-tab__dot"></span><span class="brand-tab__name">The Pantry<br>Compass</span></div>
  <div class="cream"></div>
  <nav class="crumbs"><span>Home</span><span>About</span><span class="current">Contact</span></nav>
  <h2 class="form-title">Request Information form</h2>
  <span class="form-title__rule"></span>
  <div class="field" style="left:92px;top:194px;width:229px;height:28px">Name</div>
  <div class="field" style="left:326px;top:194px;width:229px;height:28px">Phone number</div>
  <div class="field" style="left:92px;top:228px;width:229px;height:28px">Email address</div>
  <div class="field" style="left:326px;top:228px;width:229px;height:28px">Address</div>
  <div class="field" style="left:92px;top:263px;width:463px;height:36px">Member of BDL</div>
  <div class="field" style="left:92px;top:308px;width:463px;height:71px">Reason for inquiry</div>
  <div class="submit-btn">SUBMIT</div>

  <div class="band" style="top:500px;height:80px"></div>
  <span class="partner" style="left:73px;top:533px">Oakmere</span>
  <span class="partner" style="left:187px;top:535px">Brightvale</span>
  <span class="partner" style="left:305px;top:535px">Tallwick</span>
  <span class="partner" style="left:430px;top:535px">Ferncourt</span>
  <span class="partner" style="left:522px;top:535px">Quillory</span>

  <h3 class="foot-title" style="left:49px;top:604px">Contact Us</h3>
  <ul class="foot-list" style="left:49px;top:642px">
    <li><svg width="9" height="11" viewBox="0 0 9 11"><path d="M4.5 0A4 4 0 0 0 .5 4c0 3 4 7 4 7s4-4 4-7a4 4 0 0 0-4-4zm0 5.5a1.5 1.5 0 1 1 0-3 1.5 1.5 0 0 1 0 3z" fill="#c9ab1c"/></svg><span>Dolore magnam aliquam<br>quaerat voluptatem.</span></li>
    <li><svg width="10" height="10" viewBox="0 0 10 10"><path d="M2 0l2 2.5-1 1.3a6 6 0 0 0 3.2 3.2L7.5 6 10 8 8.6 10C4 10 0 6 0 1.4z" fill="#c9ab1c"/></svg><span>0800 410 22 73<br>0900 731 45 08</span></li>
    <li><svg width="10" height="8" viewBox="0 0 10 8"><rect width="10" height="8" fill="#c9ab1c"/><path d="M0 0l5 4 5-4" stroke="#fff" fill="none"/></svg><span>Thepantrycompass@mailvento.net</span></li>
  </ul>
  <h3 class="foot-title" style="left:273px;top:604px">Menu</h3>
  <ul class="foot-list foot-menu" style="left:275px;top:642px"><li>Home</li><li>About Me</li><li>Services</li><li>Blog</li><li>Contact Us</li></ul>
  <div class="foot-brand" style="left:448px;top:606px"><span class="foot-brand__dot"></span><span class="foot-brand__name">The Pantry<br>Compass</span><div class="social" aria-label="Social links"><span></span><span></span><span></span></div></div>
  <p class="copyright" style="top:780px">© 2021 &nbsp;|&nbsp; www.pantrycompass.net</p>
</section>

</body>
</html>
```